Business Card Design Project

This is a new division in our company. "Meridale Wellsite & Safety" This is a Oilfield Safety company. I have included our new logo. I also have given our other business card. We love double sided with lots of color. We like to stand out. Please DO NOT duplicate our other card and bring your design into it. See all attached files.
Reason: forgot to change this when I posted it.
Here is the correct information card.
www.meridalewellsitesafety.com
Dwayne@meridalewellsitesafety.com
Reason: revision for a few.
Reason: was traveling and need to review designs.
Oil and Gas industry. Masculine look.
Business

```html
<!DOCTYPE html>
<html lang="en">
<head>
<meta charset="utf-8">
<title>Meridale Wellsite &amp; Safety — Business Card</title>
<link rel="stylesheet" href="https://fonts.googleapis.com/css2?family=Oswald:wght@700&family=Old+Standard+TT:wght@400;700&display=swap">
<style>
  :root {
    --backdrop: #cfd0d1;
    --rust: #c4521c;
    --rust-deep: #8f2e0c;
    --rust-bright: #e0702a;
    --paper: #fbfaf7;
    --ink-red: #8a1d14;
    --brand-teal: #1f9d9a;
    --white: #ffffff;
  }
  * { margin: 0; padding: 0; box-sizing: border-box; }
  html, body { width: 1200px; height: 1200px; overflow: hidden; }
  body {
    background: var(--backdrop);
    position: relative;
  }
  .card {
    position: absolute;
    left: 170px;
    width: 860px;
    height: 491px;
    overflow: hidden;
    box-shadow: 0 6px 18px rgba(0,0,0,0.18);
  }
  /* Front side */
  .card-front { top: 80px; }
  .front-texture {
    position: absolute; inset: 0;
    background:
      radial-gradient(ellipse at 45% 40%, var(--rust-bright) 0%, var(--rust) 45%, var(--rust-deep) 100%);
  }
  .front-brand {
    position: absolute; inset: 0;
    display: flex; flex-direction: column; align-items: center; justify-content: center;
    color: var(--white);
  }
  .front-name {
    font-family: "Oswald", sans-serif;
    font-weight: 700;
    font-size: 50px;
    line-height: 1.1;
    letter-spacing: 1px;
    text-transform: uppercase;
    text-align: center;
  }
  .front-web {
    margin-top: 16px;
    padding: 6px 10px;
    border-top: 2px solid var(--white);
    border-bottom: 2px solid var(--white);
    font-family: "Old Standard TT", serif;
    font-size: 20px;
    letter-spacing: 2px;
    text-transform: uppercase;
  }
  /* Back side */
  .card-back { top: 629px; background: var(--paper); }
  .holder-name {
    position: absolute; left: 48px; top: 28px;
    font-family: "Old Standard TT", serif;
    font-weight: 700;
    font-size: 40px;
    color: var(--ink-red);
    text-transform: uppercase;
    border-bottom: 3px solid var(--ink-red);
    line-height: 1.15;
  }
  .contact-list {
    position: absolute; left: 48px; top: 104px;
    list-style: none;
    font-family: "Old Standard TT", serif;
    font-size: 28px;
    color: var(--ink-red);
  }
  .contact-list li {
    display: flex; align-items: center;
    height: 47px;
    white-space: nowrap;
  }
  .contact-icon { width: 28px; height: 28px; margin-right: 18px; flex: none; }
  .back-brand {
    position: absolute; right: 40px; top: 110px;
    font-family: "Oswald", sans-serif;
    font-weight: 700;
    font-size: 32px;
    line-height: 1.15;
    color: var(--brand-teal);
    text-transform: uppercase;
    text-align: right;
  }
  .call-band {
    position: absolute; left: 0; right: 0; bottom: 0;
    height: 100px;
    background: var(--rust);
    display: flex; align-items: center; justify-content: center;
    font-family: "Oswald", sans-serif;
    font-weight: 700;
    font-size: 46px;
    letter-spacing: 1px;
    color: var(--white);
  }
</style>
</head>
<body>

<section class="card card-front">
  <div class="front-texture" role="img" aria-label="Orange mosaic of soft overlapping squares"></div>
  <div class="front-brand">
    <div class="front-name">Meridale<br>Wellsite &amp; Safety</div>
    <div class="front-web">www.meridalewellsitesafety.com</div>
  </div>
</section>

<section class="card card-back">
  <h1 class="holder-name">Dwayne Keller</h1>
  <ul class="contact-list">
    <li>
      <svg class="contact-icon" viewBox="0 0 28 28"><circle cx="14" cy="14" r="13" fill="none" stroke="#8a1d14" stroke-width="2"/><path d="M10 8c-1 1-1.5 2.5 0 5s3.5 5 6 6c1.5.6 2.5 0 3-.8l-2.3-2.2-1.6 1c-1.5-.8-3-2.4-3.8-3.9l1-1.5L10 8z" fill="#8a1d14"/></svg>
      281-555-0147
    </li>
    <li>
      <svg class="contact-icon" viewBox="0 0 28 28"><circle cx="14" cy="14" r="13" fill="none" stroke="#8a1d14" stroke-width="2"/><path d="M11 8h7M11 8v12M11 14h5" stroke="#8a1d14" stroke-width="2.4" fill="none"/></svg>
      1-888-555-0192
    </li>
    <li>
      <svg class="contact-icon" viewBox="0 0 28 28"><circle cx="14" cy="14" r="13" fill="none" stroke="#8a1d14" stroke-width="2"/><path d="M10 8c-1 1-1.5 2.5 0 5s3.5 5 6 6c1.5.6 2.5 0 3-.8l-2.3-2.2-1.6 1c-1.5-.8-3-2.4-3.8-3.9l1-1.5L10 8z" fill="#8a1d14"/></svg>
      713-555-0163
    </li>
    <li>
      <svg class="contact-icon" viewBox="0 0 28 28"><rect x="2" y="6" width="24" height="16" fill="#8a1d14"/><path d="M2 6l12 9 12-9" stroke="#fbfaf7" stroke-width="2" fill="none"/></svg>
      Dwayne@meridalewellsitesafety.com
    </li>
    <li>
      <svg class="contact-icon" viewBox="0 0 28 28"><circle cx="14" cy="14" r="13" fill="#8a1d14"/><path d="M14 6a5 5 0 0 0-5 5c0 4 5 10 5 10s5-6 5-10a5 5 0 0 0-5-5z" fill="#fbfaf7"/><circle cx="14" cy="11" r="2" fill="#8a1d14"/></svg>
      4810 N.Ridge Road-Baytown Tx 77520
    </li>
  </ul>
  <div class="back-brand">Meridale<br>Wellsite &amp; Safety</div>
  <div class="call-band">CALL - 1-888-5-WELLSITE</div>
</section>

</body>
</html>
```